Foodcard Package Design for 10ml Food Enhancer

I have developed a product with a friend that we will be selling later this year, it is a liquid that comes in a small 10ml or 20ml bottle for sale in shops (a flavour enhancer).

A small cardboard sized backer of approximate size "A5" is the best packaging for this product.

i have attached an example of what I am looking for - the front will hold the bottle inside a small plastic case, and the back will be how to use the product / instructions.

What I am looking for is:
Strong graphic design skills to capture customers attention
Good layout of "how to use" instructions so it is clear for customer to understand
Similar "feel" to attached document as guide only

(Note: I will add the words myself, the graphics is all I need. When you design the front & back you will add Lorem ipsom text to display position of text only).

Target Market(s)

Retail & Restaurant industry

Industry/Entity Type

Retail

Font styles to use
Serif

Requirements
Must have
• Captures customers attention, high impact, sophisticated
Nice to have
• Colour, cutting edge look
Should not have
• Not cheap looking

```html
<!DOCTYPE html>
<html lang="en">
<head>
<meta charset="utf-8">
<title>The Hidden Kitchen Note – Food Card</title>
<link rel="stylesheet" href="https://fonts.googleapis.com/css2?family=Jost:wght@300;400;700;800&display=swap">
<style>
  :root{
    --ink:#000;
    --paper:#fff;
    --rule:#111;
    --potato-a:#f1e2a8; --potato-b:#c9a76a;
    --rice-a:#d9cfae; --rice-b:#7d8f4e;
    --stew-a:#5a2a18; --stew-b:#c9c3bd;
    --sauce-a:#a3261a; --sauce-b:#d9d2c9;
    --whisky-a:#d18a1f; --whisky-b:#f4ead9;
  }
  *{box-sizing:border-box;margin:0;padding:0}
  html,body{width:1200px;height:895px;overflow:hidden;background:var(--paper)}
  body{position:relative;font-family:"Jost",sans-serif;color:var(--ink)}

  .card{position:absolute;top:45px;width:451px;height:797px;border:2px solid var(--ink);border-radius:24px;background:var(--paper);overflow:hidden}
  .card--front{left:116px}
  .card--back{left:627px}

  .hang-hole{position:absolute;top:27px;left:174px;width:100px;height:34px}

  .brand-band{position:absolute;top:79px;left:0;height:150px;background:var(--ink);color:var(--paper)}
  .card--front .brand-band{width:304px}
  .card--back .brand-band{width:100%}

  .brand-lockup{position:absolute;top:28px;width:250px}
  .card--front .brand-lockup{left:40px}
  .card--back .brand-lockup{left:100px}

  .brand-name{font-weight:400;font-size:31px;line-height:34px;letter-spacing:0.2px}
  .brand-name span{display:block}
  .brand-sub{margin-top:12px;font-weight:300;font-size:17px;line-height:22px;text-transform:uppercase;letter-spacing:0.6px}

  .usage-note{position:absolute;left:45px;top:237px;font-weight:300;font-size:16px;line-height:19px;text-transform:uppercase}

  .uses-grid{position:absolute;left:45px;top:307px;display:grid;grid-template-columns:127px 127px;grid-auto-rows:91px}
  .use-label{display:flex;align-items:center;justify-content:center;text-align:center;font-weight:800;font-size:18px;line-height:22px;text-transform:uppercase}
  .use-photo{display:block}
  .use-photo--potato{background:radial-gradient(circle at 55% 50%,var(--potato-a),var(--potato-b) 90%)}
  .use-photo--rice{background:linear-gradient(160deg,#8a6a45 0 20%,var(--rice-a) 20% 50%,var(--rice-b))}
  .use-photo--stew{background:radial-gradient(circle at 50% 45%,var(--stew-a) 40%,var(--stew-b) 75%)}
  .use-photo--sauce{background:radial-gradient(circle at 50% 40%,var(--sauce-a) 45%,var(--sauce-b) 70%)}
  .use-photo--whisky{background:linear-gradient(135deg,var(--whisky-b) 20%,var(--whisky-a) 55%,#8a4b10)}

  .display-window{position:absolute;left:324px;top:79px;width:102px;height:697px;border:2px solid var(--ink);border-radius:36px}

  .options{position:absolute;left:40px;top:245px;width:370px;text-align:center}
  .options-title{font-weight:800;font-size:19px;letter-spacing:0.3px;text-transform:uppercase;line-height:34px;border-bottom:2px solid var(--rule)}
  .option{font-size:16px;line-height:19px;font-weight:400;border-bottom:2px solid var(--rule);padding:13px 8px 7px}
  .option:last-child{border-bottom:none}
  .option h3{font-weight:400;font-size:16px;text-transform:uppercase}
  .option p.gap{margin-top:18px}
  .option .gap-head{margin-top:18px}
</style>
</head>
<body>

<section class="card card--front" aria-label="Front of food card">
  <svg class="hang-hole" viewBox="0 0 100 34" aria-hidden="true">
    <path d="M8 13 H36 A14 12 0 0 1 64 13 H92 A7 7 0 0 1 92 28 H8 A7 7 0 0 1 8 13 Z" fill="none" stroke="#000" stroke-width="2"/>
  </svg>

  <div class="brand-band">
    <div class="brand-lockup">
      <h1 class="brand-name"><span>The Hidden</span><span>Kitchen Note</span></h1>
      <p class="brand-sub">Hollowell Oak Wine<br>Barrel Wood Extracts</p>
    </div>
  </div>

  <p class="usage-note">Add to boiling water<br>for farmhouse style vegetables</p>

  <div class="uses-grid">
    <div class="use-label">Mashed<br>Potatoes</div>
    <div class="use-photo use-photo--potato" role="img" aria-label="Photo of mashed potatoes on a wooden spoon"></div>
    <div class="use-photo use-photo--rice" role="img" aria-label="Photo of a rice dish with a fork"></div>
    <div class="use-label">Rice</div>
    <div class="use-label">Stews<br>Casseroles</div>
    <div class="use-photo use-photo--stew" role="img" aria-label="Photo of a beef stew in a bowl"></div>
    <div class="use-photo use-photo--sauce" role="img" aria-label="Photo of red sauce in a glass bowl with a brush"></div>
    <div class="use-label">Sauces</div>
    <div class="use-label">Whisky</div>
    <div class="use-photo use-photo--whisky" role="img" aria-label="Photo of whisky glasses with ice cubes"></div>
  </div>

  <div class="display-window" aria-label="Clear window for bottle"></div>
</section>

<section class="card card--back" aria-label="Back of food card">
  <svg class="hang-hole" viewBox="0 0 100 34" aria-hidden="true">
    <path d="M8 13 H36 A14 12 0 0 1 64 13 H92 A7 7 0 0 1 92 28 H8 A7 7 0 0 1 8 13 Z" fill="none" stroke="#000" stroke-width="2"/>
  </svg>

  <div class="brand-band">
    <div class="brand-lockup">
      <h1 class="brand-name"><span>The Hidden</span><span>Kitchen Note</span></h1>
      <p class="brand-sub">Hollowell Oak Wine<br>Barrel Wood Extracts</p>
    </div>
  </div>

  <div class="options">
    <h2 class="options-title">Try these easy options</h2>
    <div class="option">
      <h3>Mashed Potatoes</h3>
      <p>Add wooded earth and charm to mashed potatoes.<br>Can be used in place of cream &amp; butter.</p>
      <p class="gap">Add 2 drops to your bowl of mashed potatoes for an earth charm flavour.</p>
    </div>
    <div class="option">
      <h3>Rice</h3>
      <p>Or apply to boiled rice for a smoky plume”<br>Once rice is cooked stir in 2 drops and experience the difference</p>
    </div>
    <div class="option">
      <h3>Sauces</h3>
      <p>Do you make your own sauces?<br>Stir in 2 drops to your sauces for an extra level of depth.</p>
    </div>
    <div class="option">
      <h3>Stews Casseroles</h3>
      <p>Add 2 drops to your bowl of mashed potatoes for a smokey charm</p>
      <h3 class="gap-head">Perfect Whisky</h3>
      <p>Mix with water and freeze into ice cube trays.<br>Add cubes to torn ordinary whisky into a premium aged whisky</p>
    </div>
  </div>
</section>

</body>
</html>
```